Business Card for premium dental clinic

We are a premium dental clinic based in Brasov, Romania with more than 15 year on the market, providing quality dental treatment made by a team of more specialized dentists, working with modern equipment as a solution to beautiful and healthy teeth.

Our current logo for the clinic use 2 square with colors black and gold - dr Corbescu - studio, using family fonts Bodoni, Myriad Pro and Segoe Print.
Depending on the printing we used some gold CMYK background or gold foil picture background or a gold gradient.
We want a business card:
- eye catching business card
- distinguished business card
- premium design
- to keep the color scheme of black and gold
- to attract the customers to spent time reading the information
- modern concept

```html
<!DOCTYPE html>
<html lang="en">
<head>
<meta charset="utf-8">
<title>dr Corbescu studio – business card</title>
<link href="https://fonts.googleapis.com/css2?family=Questrial&display=swap" rel="stylesheet">
<style>
  :root {
    --page: #ffffff;
    --card-black: #221f20;
    --gold: #f0b323;
    --gold-light: #f7c84a;
    --gold-deep: #d9901a;
  }
  * { margin: 0; padding: 0; box-sizing: border-box; }
  html, body {
    width: 902px; height: 1200px; overflow: hidden;
    background: var(--page);
    font-family: "Questrial", "Century Gothic", sans-serif;
  }
  .canvas { position: relative; width: 902px; height: 1200px; }

  .card {
    position: absolute;
    width: 745px; height: 437px;
    background: var(--card-black);
    box-shadow: 3px 4px 6px rgba(0,0,0,0.22);
    overflow: hidden;
  }
  .card--back  { left: 79px; top: 129px; }
  .card--front { left: 78px; top: 632px; height: 434px; }

  .gold-foil {
    position: absolute; left: 0; top: 0; height: 100%;
    background: linear-gradient(135deg, var(--gold-light) 0%, var(--gold) 45%, var(--gold-deep) 100%);
  }
  .card--back .gold-foil  { width: 158px; }
  .card--front .gold-foil { width: 350px; }

  .wordmark { position: absolute; color: var(--gold); font-weight: 400; line-height: 1.15; }
  .card--back .wordmark { left: 180px; top: 240px; }
  .card--back .wordmark__name { font-size: 20px; }
  .card--back .wordmark__tag  { font-size: 13px; margin-top: 4px; }
  .card--front .wordmark { left: 386px; top: 170px; }
  .card--front .wordmark__name { font-size: 46px; }
  .card--front .wordmark__tag  { font-size: 26px; margin-top: 14px; }

  .identity { position: absolute; left: 411px; top: 76px; color: var(--gold); }
  .identity__name { font-size: 27px; letter-spacing: 0.3px; line-height: 1.1; }
  .identity__role { font-size: 17px; line-height: 1.2; }

  .address {
    position: absolute; left: 411px; top: 227px;
    color: var(--gold); font-size: 16.5px; line-height: 21px; font-style: normal;
  }

  .contacts { position: absolute; left: 411px; top: 313px; list-style: none; color: var(--gold); }
  .contacts__item { display: flex; align-items: center; height: 22px; font-size: 16.5px; }
  .contacts__icon { width: 12px; height: 12px; margin-right: 12px; fill: var(--gold); flex: none; }
</style>
</head>
<body>
<main class="canvas">

  <section class="card card--back" aria-label="Card back with contact details">
    <div class="gold-foil" role="img" aria-label="Gold foil texture"></div>

    <div class="wordmark">
      <div class="wordmark__name">dr. corbescu studio</div>
      <div class="wordmark__tag">dental clinic</div>
    </div>

    <div class="identity">
      <h1 class="identity__name">DR. CORBESCU</h1>
      <p class="identity__role">Dental specialist</p>
    </div>

    <address class="address">3rd floor, Lunga Street no<br>48 Brasov, Romania</address>

    <ul class="contacts">
      <li class="contacts__item">
        <svg class="contacts__icon" viewBox="0 0 12 12" aria-hidden="true"><path d="M2.4 0.5l2 2.2-1 1.3c.7 1.6 2 2.9 3.6 3.6l1.3-1 2.2 2-1.1 2.1C5 10.5 1.5 7 .4 1.6z"/></svg>
        0268 415 902
      </li>
      <li class="contacts__item">
        <svg class="contacts__icon" viewBox="0 0 12 12" aria-hidden="true"><path d="M0 2.5h12v7H0z M0.8 3.2L6 7l5.2-3.8" fill="var(--gold)" stroke="var(--card-black)" stroke-width="0.9"/></svg>
        contact@corbescustudio.ro
      </li>
      <li class="contacts__item">
        <svg class="contacts__icon" viewBox="0 0 12 12" aria-hidden="true"><circle cx="6" cy="6" r="5.5"/><path d="M3 3.5c1 .3 1.5 1 1.2 2 .8.4 1 1.3.4 2.3M7.5 1.5c-.3 1 .3 1.8 1.3 1.8.5 1 0 2-.8 2.4" stroke="var(--card-black)" stroke-width="1" fill="none"/></svg>
        www.corbescustudio.ro
      </li>
    </ul>
  </section>

  <section class="card card--front" aria-label="Card front with clinic name">
    <div class="gold-foil" role="img" aria-label="Gold foil texture"></div>
    <div class="wordmark">
      <div class="wordmark__name">dr. corbescu</div>
      <div class="wordmark__tag">studio · dental clinic</div>
    </div>
  </section>

</main>
</body>
</html>
```